Watch brand needs new business cards

Fernhollow Clock Company are looking for a new business card design incorporating our logo and brand colours as per our website.

Design should be 90x55mm with 3mm print margin from edges and 3mm external bleed.

Card should be double sided, e.g. logo one side, personal details on the other.

Logo will be provided as a vector.

The card must be able to show:
- Staff name
- Position
- Office Address
- Email
- Telephone number
- Website address

Final work must be provided in an editable format to allow us to add staff details (e.g. an AI or PSD file).

Industry/Entity Type

Business

```html
<!DOCTYPE html>
<html lang="en">
<head>
<meta charset="utf-8">
<title>Fernhollow Clock Company — Business Cards</title>
<link rel="stylesheet" href="https://fonts.googleapis.com/css2?family=Poppins:wght@300;400;600&display=swap">
<style>
  :root {
    --backdrop: #ecebe8;
    --ink: #141414;
    --paper: #f7f7f5;
    --silver: #e4e4e4;
    --muted: #3a3a3a;
  }
  * { box-sizing: border-box; margin: 0; padding: 0; }
  html, body { width: 1200px; height: 775px; overflow: hidden; }
  body {
    background: var(--backdrop);
    font-family: "Poppins", sans-serif;
    position: relative;
  }
  .card {
    position: absolute;
    top: 228px;
    width: 520px;
    height: 318px;
    border-radius: 4px;
    box-shadow: 0 6px 18px rgba(0,0,0,0.12);
  }
  .card--front { left: 60px; background: var(--ink); color: var(--silver); }
  .card--back  { left: 620px; background: var(--paper); color: var(--ink); }

  .brand {
    position: absolute;
    display: flex;
    flex-direction: column;
    align-items: center;
    font-weight: 600;
    text-transform: uppercase;
  }
  .brand__mark {
    border-radius: 50%;
    border: 3px solid currentColor;
  }
  .brand__name { letter-spacing: 0.06em; line-height: 1; }
  .brand__sub { letter-spacing: 0.3em; line-height: 1; }

  .card--front .brand { left: 0; right: 0; top: 82px; }
  .card--front .brand__mark { width: 58px; height: 58px; margin-bottom: 18px; }
  .card--front .brand__name { font-size: 40px; }
  .card--front .brand__sub { font-size: 12px; margin-top: 10px; }

  .card--back .brand { right: 34px; top: 120px; width: 200px; }
  .card--back .brand__mark { width: 40px; height: 40px; border-width: 2px; margin-bottom: 12px; }
  .card--back .brand__name { font-size: 22px; }
  .card--back .brand__sub { font-size: 8px; margin-top: 7px; }

  .staff {
    position: absolute;
    left: 34px;
    top: 32px;
    padding-left: 12px;
    border-left: 6px solid var(--ink);
  }
  .staff__name { font-size: 20px; font-weight: 300; line-height: 1.1; }
  .staff__name strong { font-weight: 600; }
  .staff__role { font-size: 11px; font-weight: 300; color: var(--muted); margin-top: 2px; }

  .contact {
    position: absolute;
    left: 34px;
    top: 168px;
    list-style: none;
    font-size: 11px;
    font-weight: 400;
    color: var(--muted);
  }
  .contact li { display: flex; align-items: center; gap: 10px; height: 22px; }
  .contact svg { width: 10px; height: 10px; fill: var(--ink); flex: none; }
</style>
</head>
<body>
  <section class="card card--front" aria-label="Card front">
    <div class="brand">
      <span class="brand__mark"></span>
      <span class="brand__name">Fernhollow</span>
      <span class="brand__sub">Clock Company</span>
    </div>
  </section>

  <section class="card card--back" aria-label="Card back">
    <div class="staff">
      <p class="staff__name">Staff <strong>Name</strong></p>
      <p class="staff__role">Job Title</p>
    </div>

    <ul class="contact">
      <li>
        <svg viewBox="0 0 10 10"><path d="M5 0a3.5 3.5 0 0 0-3.5 3.5C1.5 6 5 10 5 10s3.5-4 3.5-6.5A3.5 3.5 0 0 0 5 0zm0 4.8a1.3 1.3 0 1 1 0-2.6 1.3 1.3 0 0 1 0 2.6z"/></svg>
        Office Address
      </li>
      <li>
        <svg viewBox="0 0 10 10"><path d="M0 2h10v6H0z M0.6 2.4 5 5.6l4.4-3.2" stroke="#f7f7f5" stroke-width="0.8"/></svg>
        Email
      </li>
      <li>
        <svg viewBox="0 0 10 10"><rect x="0" y="0" width="10" height="10" rx="1.5"/><path d="M3 2.2c.4 0 .8 1.2.6 1.6-.2.3-.5.3-.3.8.3.6.8 1.1 1.4 1.4.5.2.5-.1.8-.3.4-.2 1.6.2 1.6.6 0 .8-.8 1.5-1.6 1.3C3.8 7.3 2.7 6.2 2.3 4.5 2 3.2 2.4 2.2 3 2.2z" fill="#f7f7f5"/></svg>
        Telephone number
      </li>
      <li>
        <svg viewBox="0 0 10 10"><circle cx="5" cy="5" r="5"/><path d="M0 5h10M5 0c-2 2.5-2 7.5 0 10M5 0c2 2.5 2 7.5 0 10" stroke="#f7f7f5" stroke-width="0.6" fill="none"/></svg>
        Website address
      </li>
    </ul>

    <div class="brand">
      <span class="brand__mark"></span>
      <span class="brand__name">Fernhollow</span>
      <span class="brand__sub">Clock Company</span>
    </div>
  </section>
</body>
</html>
```